Postcard double sided

Title: DWIGHT'S REVENGE

Why would Dwight Kessler align himself with Gordon Pruett?

(photo of two guys)

Dwight approached elected officials that he wanted to run for office, but did not have money to finance his campaign. He wanted other elected officials to finance his campaign. Everyone told him that they would help him get the vote out, but that he needed to finance his own race.

In comes Gordon Pruett.

Gordon Pruett who has a pay to play scheme over at the City, told Dwight he would finance his campaign on one condition.

He needed to run against Steven Hulse.

Why would Dwight want to run with no money?

Backside

DWIGHT'S REVENGE

Dwight decided to run because no one on the school board would terminate Dwight's ex and her new boyfriend who both work for the school district. His ex even filed criminal charges against him that are still pending.

Mug Shot facing left (name the charges Criminal Trespass , and Criminal Mischief (highlight bold letters use two lines) mug shot facing right

Complaint one (then photo with full face) Compliant 2)
(showcharges)

Dwight's ultimate goal is to terminate his ex and her new boyfriend if elected.
Plus Gordon Pruett needs the majority on the school board to do what he does bet.

Kickbacks for Contracts.

They will hire their own contractors!
Say "No" to Dwight's Revenge and Gordon Pruett Money Grab!

Title On Back: all caps: DOMESTIC VIOLENCE

```html
<!DOCTYPE html>
<html lang="en">
<head>
<meta charset="utf-8">
<title>Dwight's Revenge – Postcard</title>
<link rel="stylesheet" href="https://fonts.googleapis.com/css2?family=Montserrat:ital,wght@1,800;1,900&family=Lato:wght@400;700;900&display=swap">
<style>
  :root{
    --backdrop:#a2a7b2;
    --red:#c41e24;
    --red-dark:#8e1116;
    --navy:#14204a;
    --gold:#f2b632;
    --ink:#1a1a1a;
    --black:#141414;
    --white:#ffffff;
    --paper:#fbfbfb;
  }
  *{box-sizing:border-box;margin:0;padding:0}
  html,body{width:1200px;height:1200px;overflow:hidden}
  body{background:var(--backdrop);font-family:"Lato",sans-serif;position:relative}
  .card{position:absolute;overflow:hidden;background:var(--white);box-shadow:0 18px 40px rgba(0,0,0,.35)}
  .card--front{left:21px;top:205px;width:565px;height:731px}
  .card--back{left:615px;top:203px;width:564px;height:729px}
  .abs{position:absolute}
  .headline{font-family:"Montserrat",sans-serif;font-weight:900;font-style:italic;color:var(--white);text-align:center;width:100%;letter-spacing:.3px;white-space:nowrap}
  .header{left:0;top:0;width:100%;height:50px;background:linear-gradient(90deg,var(--red),#d82a2f 50%,var(--red))}
  .header .headline{font-size:34px;line-height:50px}
  .header-rule{left:0;top:54px;width:100%;height:4px;background:var(--red)}
  .bg-shapes{left:0;top:0}

  /* front */
  .question{right:20px;top:68px;text-align:right;font-weight:900;font-size:21px;line-height:21px;color:var(--ink);text-transform:uppercase}
  .question .mark{border-bottom:3px solid var(--red);padding-bottom:1px}
  .story{left:20px;top:370px;width:415px;color:var(--white);font-size:15px;line-height:20.5px;font-weight:700}
  .in-comes{left:20px;top:487px;color:var(--white);font-weight:700;font-size:21px;line-height:26px}
  .in-comes .who{color:var(--gold);border-bottom:3px solid var(--red);padding-right:2px}
  .condition{right:20px;top:535px;width:320px;text-align:right;color:var(--white);font-size:15px;line-height:22px;font-weight:700}
  .condition .em{border-bottom:2px solid var(--red);padding-bottom:1px}
  .opponent-box{left:87px;top:621px;width:387px;height:38px;background:var(--white);text-align:center;font-weight:700;font-size:16px;line-height:38px;color:var(--navy)}
  .opponent-box .name{color:var(--red)}
  .footer-front{left:0;top:673px;width:100%;height:58px;background:var(--black)}
  .footer-front .headline{font-size:19px;line-height:20px;padding-top:8px}

  /* back */
  .intro{left:0;top:58px;width:100%;text-align:center;font-size:14px;line-height:17.5px;color:var(--ink);font-weight:700;padding-top:6px}
  .photo-band{left:0;top:120px;width:100%;height:228px;background:linear-gradient(180deg,var(--red-dark),#a3161b)}
  .mugshot{border:2px solid #d9d9d9;background:linear-gradient(180deg,#a7a9ac,#7b7f84);box-shadow:0 3px 8px rgba(0,0,0,.5)}
  .charge-badge{left:149px;top:135px;width:262px;height:46px;background:var(--white);border:3px solid var(--red);box-shadow:0 0 0 2px var(--white),0 3px 8px rgba(0,0,0,.4);text-align:center;color:var(--red);font-weight:900;font-size:15px;line-height:17px;padding-top:4px}
  .docs{left:0;top:348px;width:100%;height:149px;background:var(--paper)}
  .complaint{top:10px;width:262px;height:132px;font-size:5.2px;line-height:6.6px;color:#333;font-family:"Lato",sans-serif}
  .complaint p{margin-bottom:3px}
  .complaint .row{display:flex;justify-content:space-between;align-items:flex-end}
  .complaint .sig-line{border-top:.6px solid #333;width:95px;margin-top:10px;padding-top:1px}
  .complaint .date{font-size:9px;line-height:11px}
  .goal-band{left:0;top:497px;width:100%;height:157px;background:var(--black)}
  .goal{left:0;top:515px;width:100%;text-align:center;color:var(--white);font-weight:700;font-size:13.6px;line-height:17px}
  .kickbacks{left:22px;top:563px;color:var(--white);font-family:"Montserrat",sans-serif;font-weight:900;font-style:italic;font-size:21px;line-height:28px;border-bottom:3px solid var(--red)}
  .hire{left:22px;top:597px;color:var(--white);font-size:15px;font-weight:700}
  .say-no{left:362px;top:599px;font-family:"Montserrat",sans-serif;font-weight:900;font-style:italic;font-size:33px;color:var(--red);line-height:46px}
  .footer-back{left:0;top:654px;width:100%;height:75px;background:linear-gradient(90deg,var(--red),#d82a2f 50%,var(--red))}
  .footer-back .headline{font-size:23px;line-height:28px;padding-top:10px}
</style>
</head>
<body>

<section class="card card--front" aria-label="Postcard front">
  <svg class="abs bg-shapes" width="565" height="731" viewBox="0 0 565 731">
    <defs>
      <linearGradient id="fadeNavy" x1="0" y1="0" x2="0" y2="1">
        <stop offset="0" stop-color="#14204a" stop-opacity="0"/>
        <stop offset="1" stop-color="#14204a" stop-opacity="1"/>
      </linearGradient>
      <linearGradient id="photoTone" x1="0" y1="0" x2="1" y2="1">
        <stop offset="0" stop-color="#3d5aa0"/>
        <stop offset=".5" stop-color="#5d6270"/>
        <stop offset="1" stop-color="#2c3f7a"/>
      </linearGradient>
    </defs>
    <rect x="0" y="85" width="565" height="500" fill="url(#photoTone)" role="img" aria-label="Photo of Dwight Kessler and Gordon Pruett smiling in suits in front of a campaign backdrop"/>
    <polygon points="0,60 565,60 565,240 0,85" fill="#ffffff"/>
    <polygon points="0,88 504,228 504,236 0,96" fill="var(--gold)"/>
    <rect x="0" y="300" width="565" height="120" fill="url(#fadeNavy)"/>
    <rect x="0" y="420" width="565" height="253" fill="var(--navy)"/>
    <polygon points="565,400 565,673 0,673 0,625" fill="var(--red)"/>
  </svg>
  <div class="abs header"><h1 class="headline">DWIGHT'S REVENGE</h1></div>
  <h2 class="abs question">Why would Dwight Kessler<br>align himself<br>with <span class="mark">Gordon Pruett?</span></h2>
  <p class="abs story">Dwight approached elected officials that he wanted to run for office, but did not have money to finance his campaign. He wanted other elected officials to finance his campaign. Everyone told him that they would help him get the vote out, but that he needed to finance his own race.</p>
  <p class="abs in-comes">IN COMES<br><span class="who">Gordon Pruett.</span></p>
  <p class="abs condition">Gordon Pruett who has a pay to play scheme over at the City, told Dwight he would finance his campaign on <span class="em">ONE CONDITION:</span></p>
  <p class="abs opponent-box">HE NEEDED TO RUN AGAINST <span class="name">STEVEN HULSE</span></p>
  <div class="abs footer-front"><p class="headline">WHY WOULD DWIGHT WANT TO RUN<br>WITH NO MONEY?</p></div>
</section>

<section class="card card--back" aria-label="Postcard back">
  <div class="abs header"><h1 class="headline">DOMESTIC VIOLENCE</h1></div>
  <p class="abs intro">Dwight decided to run because no one on the school board would terminate<br>Dwight's ex and her new boyfriend who both work for the school district.<br>His ex even filed criminal charges against him that are still pending.</p>
  <div class="abs photo-band"></div>
  <div class="abs mugshot" style="left:31px;top:134px;width:99px;height:124px" role="img" aria-label="Mug shot, profile facing left"></div>
  <div class="abs mugshot" style="left:231px;top:192px;width:100px;height:125px" role="img" aria-label="Mug shot, full face"></div>
  <div class="abs mugshot" style="left:432px;top:134px;width:99px;height:125px" role="img" aria-label="Mug shot, profile facing right"></div>
  <p class="abs charge-badge">CRIMINAL TRESPASS<br>&amp; CRIMINAL MISCHIEF</p>

  <div class="abs docs">
    <article class="abs complaint" style="left:14px">
      <div class="row"><p>THE STATE OF TEXAS<br>COUNTY OF REDFIELD</p><p>CR-21-40712-B</p></div>
      <p>IN THE NAME AND BY AUTHORITY OF THE STATE OF TEXAS:<br>Before me, the undersigned affiant, who under oath says, has good reason to believe that in Redfield County, Texas,</p>
      <p>DWIGHT KESSLER, on or about the 14th day of May, 2021, did intentionally enter property of another, namely Carla Benton, without consent, after notice that entry was forbidden.</p>
      <div class="row"><p>AGAINST THE PEACE AND DIGNITY OF THE STATE.</p><p>FILED FOR RECORD<br>Martin Ellery, County Clerk</p></div>
      <div class="row"><p>Sworn to and subscribed before me on<br><span class="date">03-09-2021</span></p><p class="sig-line">Assistant Criminal District Attorney</p></div>
    </article>
    <article class="abs complaint" style="left:288px">
      <div class="row"><p>THE STATE OF TEXAS<br>COUNTY OF REDFIELD</p><p>CR-21-40713-B</p></div>
      <p>IN THE NAME AND BY AUTHORITY OF THE STATE OF TEXAS:<br>Before me, the undersigned affiant, who under oath says, has good reason to believe that in Redfield County, Texas,</p>
      <p>DWIGHT KESSLER, on or about the 14th day of May, 2021, did intentionally damage garage lights owned by Carla Benton, without consent, causing a small loss.</p>
      <div class="row"><p>AGAINST THE PEACE AND DIGNITY OF THE STATE.</p><p>FILED FOR RECORD<br>Martin Ellery, County Clerk</p></div>
      <div class="row"><p>Sworn to and subscribed before me on<br><span class="date">03-09-2021</span></p><p class="sig-line">Assistant Criminal District Attorney</p></div>
    </article>
  </div>

  <div class="abs goal-band"></div>
  <svg class="abs" style="left:0;top:587px" width="564" height="67" viewBox="0 0 564 67">
    <polygon points="355,0 564,0 564,67 325,67" fill="#ffffff"/>
  </svg>
  <p class="abs goal">Dwight's ultimate goal is to terminate his ex and her new boyfriend if elected.<br>Plus Gordon Pruett needs the majority on the school board to do what he does bet.</p>
  <p class="abs kickbacks">Kickbacks for Contracts.</p>
  <p class="abs hire">They will hire their own contractors!</p>
  <p class="abs say-no">Say "No"</p>
  <div class="abs footer-back"><p class="headline">to Dwight's Revenge and<br>Gordon Pruett Money Grab!</p></div>
</section>

</body>
</html>
```